Lumara Health & Wellness Business Card Design

We would like to create business cards matching with our new logo design. The card should be professional looking but still have a playful side and something that would be eye catching. We are planing to open a luxury medical spa and looking to create a design based on this new logo. We are looking for a design that shows off luxury but not be gold in color. Also, while we are a more female oriented medical center we do have men that come in for our services and it should be be too feminine.

Target Market(s)

Health & Wellness. Medical patients. Luxury spa

Industry/Entity Type

Health And Wellness

Contact Information for Business Card

It should have the logo design in the front of card and back of card should have our contact information. Our current colors are peach/ coral, teal, and gray. We are looking for a modern looking design.

Font styles to use
Script

Colors
32a6d6
e667a6
86cfc6
fece3e

Requirements
Must have
• It should have our logo design. We would prefer to have a more modern look to the card.
Nice to have
• Eye-Catching Design on the personable side but still classy.
Should not have
• At this point we are looking for the best design. It should not have color purple.

```html
<!DOCTYPE html>
<html lang="en">
<head>
<meta charset="utf-8">
<title>Lumara Health &amp; Wellness Business Card</title>
<link href="https://fonts.googleapis.com/css2?family=Great+Vibes&family=Cabin:ital,wght@0,400;0,500;1,400&family=Cormorant+SC:wght@500&display=swap" rel="stylesheet">
<style>
  :root {
    --stage: #e667a6;
    --teal: #5fbccd;
    --teal-light: #86cfc6;
    --photo-tone: #a9d3cf;
    --ink: #111111;
    --yellow: #fece3e;
    --orange: #fbaa3a;
    --coral: #e8778f;
    --white: #ffffff;
    --icon-blue: #32a6d6;
    --flower-tone: #e2b548;
  }
  * { margin: 0; padding: 0; box-sizing: border-box; }
  html, body { width: 1200px; height: 1200px; overflow: hidden; }
  body { background: var(--stage); position: relative; font-family: "Cabin", sans-serif; }

  .card { position: absolute; width: 840px; height: 480px; overflow: hidden; }

  /* Front */
  .card-front { left: 72px; top: 94px; background: var(--teal); }
  .portrait {
    position: absolute; left: 0; top: 0; width: 520px; height: 100%;
    background: linear-gradient(90deg, var(--photo-tone) 0%, var(--photo-tone) 55%, rgba(134,207,198,0.6) 80%, rgba(95,188,205,0) 100%);
  }
  .front-brand {
    position: absolute; left: 440px; top: 190px; width: 360px;
    color: var(--ink); font-family: "Cormorant SC", serif; font-weight: 500;
    text-align: center; line-height: 1.05;
  }
  .front-brand .brand-name { display: block; font-size: 64px; letter-spacing: 2px; }
  .front-brand .brand-line { display: block; font-size: 30px; letter-spacing: 1px; }

  /* Back */
  .card-back {
    left: 288px; top: 627px;
    background: linear-gradient(180deg, var(--yellow) 0%, var(--yellow) 45%, var(--orange) 100%);
  }
  .title-band {
    position: absolute; left: 0; top: 54px; width: 100%; height: 133px;
    background: linear-gradient(90deg, rgba(232,119,143,0) 25%, rgba(232,119,143,0.85) 55%, var(--coral) 75%);
  }
  .band-title {
    position: absolute; right: 60px; top: 16px;
    font-family: "Great Vibes", cursive; font-size: 68px; color: var(--white); line-height: 1;
  }
  .band-subtitle {
    position: absolute; right: 60px; top: 94px;
    font-style: italic; font-size: 19px; color: var(--white);
  }
  .still-life {
    position: absolute; left: 0; top: 205px; width: 420px; height: 240px;
    background: radial-gradient(ellipse at 60% 45%, var(--flower-tone) 0%, rgba(226,181,72,0.5) 45%, rgba(251,170,58,0) 75%);
  }
  .contact { position: absolute; right: 56px; top: 262px; list-style: none; }
  .contact li {
    display: flex; align-items: center; justify-content: flex-end;
    color: var(--ink); font-size: 21px; letter-spacing: 0.6px; line-height: 1.12;
    margin-bottom: 19px;
  }
  .contact .text { text-align: right; }
  .contact svg { width: 32px; height: 32px; margin-left: 18px; flex: none; }
</style>
</head>
<body>

<section class="card card-front">
  <div class="portrait" role="img" aria-label="Soft-toned beauty portrait photograph"></div>
  <div class="front-brand">
    <span class="brand-name">Lumara</span>
    <span class="brand-line">Health &amp; Wellness</span>
  </div>
</section>

<section class="card card-back">
  <div class="title-band">
    <div class="band-title">Lorem Ipsum</div>
    <div class="band-subtitle">Dummy Text</div>
  </div>
  <div class="still-life" role="img" aria-label="Lily flower with smooth black spa stones"></div>
  <ul class="contact">
    <li>
      <span class="text">(555) 214-7730</span>
      <svg viewBox="0 0 32 32" aria-hidden="true"><circle cx="16" cy="16" r="14" fill="none" stroke="var(--icon-blue)" stroke-width="2.2"/><path d="M11 9c1-1 2-1 2.6 0l1.6 2.6c.4.7.2 1.4-.4 1.9l-1 .8c.8 2 2.4 3.6 4.4 4.4l.8-1c.5-.6 1.2-.8 1.9-.4l2.6 1.6c1 .6 1 1.6 0 2.6-1.4 1.4-3.4 1.6-5.6.4-3-1.6-5.6-4.2-7.2-7.2-1.2-2.2-1-4.2.3-5.7z" fill="var(--icon-blue)"/></svg>
    </li>
    <li>
      <span class="text">info@lumarahealth.com</span>
      <svg viewBox="0 0 32 32" aria-hidden="true"><rect x="3" y="8" width="26" height="18" rx="2" fill="var(--icon-blue)"/><path d="M4 10l12 8 12-8" fill="none" stroke="var(--yellow)" stroke-width="2"/></svg>
    </li>
    <li>
      <span class="text">42 Alder Lane, Suite 4<br>Brookfield, NJ 07999</span>
      <svg viewBox="0 0 32 40" aria-hidden="true" style="height:40px"><path d="M16 2c-5.5 0-9.5 4-9.5 9.3 0 6.7 9.5 17.7 9.5 17.7s9.5-11 9.5-17.7C25.5 6 21.5 2 16 2z" fill="var(--icon-blue)"/><circle cx="16" cy="11.5" r="3.6" fill="var(--yellow)"/><ellipse cx="16" cy="33" rx="13" ry="4" fill="none" stroke="var(--icon-blue)" stroke-width="1.8"/></svg>
    </li>
  </ul>
</section>

</body>
</html>
```